Technology Company Web Design Project

We are working with BrimCore. They are a technology company and in need of a new website design.
BrimCore helps companies control who (or what) can access which information inside their systems — and under what conditions. Think of them as the traffic controller for digital access and data permissions.
Instead of letting every app, employee, or AI bot freely connect to everything, GatewardIQ makes sure:
• Each one only gets access to what it actually needs.
• That access follows company rules automatically.
• Those rules are enforced the same way everywhere — across apps, servers, and even AI tools.
Some competitor sites to use for inspiration:
https://www.trovanexus.example/en/lp/ac/trovaspire.html
https://www.clearrulekeeper.example
https://www.vondix.example
Thank you for taking the time to consider designing a website for us. We are web developers based in Stockton and Los Angeles, CA, USA. Most of our projects go through the same process. Understanding this process may help you win a project with us. We custom-code all of our websites in-house. We don’t have any requirements as to what tools you use for your design, but we prefer Drafton files. For any design that we label as four-stars, we send it to the client for review. The client picks the final design they want us to use. Once we complete this process, we will continue to show additional clients all the four-star sites and purchase them later. Your designs will have multiple chances to sell. For better chances of success, we ask that you follow these guidelines.
IMAGES:
If you use any images or icons in the design, we ask that you have a link to the asset so we can purchase the image/icon. Most of the designs we submit do not have the customer’s images on them unless they have some great images. Be creative; show us the feeling you are trying to portray with your image choices. Use any royalty-free site you choose. We subscribe to Kelvaro and mainly use their images, but we can purchase images outside of Kelvaro.
PLEASE NOTE: we will not submit designs to clients with watermarks on the images.
FONTS:
We ask that you identify the fonts used in the design. This can be done in a message if you want. We typically use Quillny Fonts and Kelvaro Fonts.
CONTENT:
We're always open to different content and ideas. We often submit designs with stock images so the client can see our vision. We typically take pictures after the website launch to use their images with our vision. Lorem Ipsum is fine for paragraphs, but we ask that you write the headers in correct English. We want to be able to show the vision and identify the sections of the website.
INSPIRATION:
We typically add a couple of links in the brief of websites we like to help you get started in your design.
REVISIONS:
We do not often ask for revisions of the designs unless we see something in the design that may not appeal to the client. If there are slight changes that we want to make, we do that in the development process.
FEEDBACK:
We rarely give feedback on designs during the design process. We are working on many website projects and do not have the time to provide feedback. We usually respond if your request is well thought out and asks specific questions, but a note asking “feedback, please” usually goes unanswered.

```html
<!DOCTYPE html>
<html lang="en">
<head>
<meta charset="utf-8">
<title>BrimCore — Access Control Platform</title>
<link rel="stylesheet" href="https://fonts.googleapis.com/css2?family=Montserrat:wght@500;600;700;800&family=Poppins:wght@400;500;600&family=Great+Vibes&display=swap">
<style>
:root{
  --navy:#1c3557;
  --navy-dark:#13294a;
  --orange:#ee7d2b;
  --ink:#1f2a3a;
  --text:#4a5261;
  --muted:#8a909a;
  --light:#f3f4f6;
  --white:#ffffff;
}
*{box-sizing:border-box;margin:0;padding:0}
html,body{width:1200px;height:4960px;overflow:hidden}
body{font-family:"Poppins",sans-serif;color:var(--text);background:var(--white);position:relative}
h1,h2,h3,h4{font-family:"Montserrat",sans-serif;color:var(--ink)}
.brand{display:flex;align-items:center;gap:12px;font-family:"Montserrat",sans-serif;font-weight:800;color:var(--navy);white-space:nowrap}
.brand .mark{background:var(--orange);border-radius:4px}
.pill{display:inline-flex;align-items:center;justify-content:center;border-radius:40px;font-family:"Montserrat",sans-serif;font-weight:700;font-size:20px;letter-spacing:.5px;text-transform:uppercase;color:var(--white);white-space:nowrap}
.pill.orange{background:var(--orange)}
.pill.navy{background:var(--navy)}
.orange-t{color:var(--orange)}

/* header */
.site-header{position:absolute;left:0;top:0;width:1200px;height:124px;background:var(--white)}
.site-header .brand{position:absolute;left:40px;top:34px;font-size:38px}
.site-header .brand .mark{width:40px;height:40px}
.search{position:absolute;left:846px;top:30px;width:180px;height:28px;border:1px solid #cfd3d9;border-radius:14px;font-size:12px;color:var(--muted);padding:5px 14px}
.signin{position:absolute;left:1042px;top:30px;width:110px;height:28px;font-size:12px;border-radius:14px;background:var(--navy);color:#fff;text-align:center;line-height:28px;font-weight:500}
.nav{position:absolute;right:40px;top:76px;display:flex;gap:40px;font-size:14px;font-family:"Montserrat",sans-serif;font-weight:600;color:var(--ink);white-space:nowrap}
.nav .active{color:var(--orange)}

/* hero */
.hero{position:absolute;left:0;top:124px;width:1200px;height:740px;background:linear-gradient(100deg,#0b1626 0%,#1d3a5c 40%,#2d5479 70%,#12263f 100%)}
.hero .welcome{position:absolute;left:716px;top:180px;font-family:"Great Vibes",cursive;font-size:56px;color:var(--orange);white-space:nowrap}
.hero h1{position:absolute;left:712px;top:244px;font-size:78px;font-weight:800;color:#fff;letter-spacing:1px;line-height:1;white-space:nowrap}
.hero p{position:absolute;left:716px;top:348px;width:440px;font-size:18px;line-height:1.5;color:#fff}
.hero .pill{position:absolute;left:716px;top:472px;width:240px;height:64px}

.features{position:absolute;left:64px;top:760px;width:1072px;height:344px;background:#fff;border-radius:40px;box-shadow:0 10px 40px rgba(20,40,70,.12);display:flex;justify-content:space-around;padding:64px 40px 0}
.feature{width:220px;text-align:center}
.feature .icon{width:128px;height:128px;border-radius:50%;margin:0 auto 22px;display:flex;align-items:center;justify-content:center;border:8px solid #e6e8ec}
.feature .icon.orange{background:var(--orange)}
.feature .icon.navy{background:var(--navy)}
.feature h3{font-size:20px;font-weight:600;line-height:1.3;color:var(--ink);text-transform:uppercase}

/* welcome */
.welcome-block{position:absolute;left:0;top:1104px;width:1200px;height:560px}
.welcome-block .emblem{position:absolute;left:220px;top:100px;width:240px;height:150px;background:radial-gradient(circle,#cdd6e3,#e9edf2);border-radius:20px}
.welcome-block h2{position:absolute;left:100px;top:292px;width:480px;text-align:center;font-size:58px;font-weight:700;line-height:1.2;color:var(--navy);white-space:nowrap}
.welcome-block .lead{position:absolute;left:612px;top:88px;width:540px;font-size:20px;font-weight:600;color:var(--ink);line-height:1.4}
.welcome-block .body{position:absolute;left:612px;top:170px;width:540px;font-size:16px;line-height:1.6}
.welcome-block .pill{position:absolute;left:612px;top:394px;width:220px;height:60px}

/* platform */
.platform{position:absolute;left:0;top:1664px;width:1200px;height:628px;background:var(--light)}
.platform h2{position:absolute;left:64px;top:104px;font-size:50px;font-weight:600;line-height:1.2;color:var(--navy);white-space:nowrap}
.platform p{position:absolute;left:64px;top:316px;width:340px;font-size:16px;line-height:1.6}
.platform .pill{position:absolute;left:64px;top:430px;width:260px;height:56px;font-size:16px}
.slide{position:absolute;top:116px;width:296px;height:396px;border-radius:20px;overflow:hidden}
.slide .cap{position:absolute;left:0;bottom:0;width:100%;padding:22px 24px;font-family:"Montserrat",sans-serif;font-weight:600;font-size:20px;color:#fff;white-space:nowrap;background:linear-gradient(transparent,rgba(10,20,35,.8))}
.arrow{position:absolute;width:56px;height:56px;border-radius:50%;display:flex;align-items:center;justify-content:center}

/* capabilities */
.capabilities{position:absolute;left:0;top:2292px;width:1200px;height:800px}
.capabilities h2{position:absolute;left:64px;top:110px;font-size:56px;font-weight:700;line-height:1.15;color:var(--navy)}
.capabilities .intro{position:absolute;left:490px;top:118px;width:660px;font-size:15px;line-height:1.7}
.capabilities .photo{position:absolute;left:64px;top:280px;width:376px;height:396px;background:linear-gradient(135deg,#3b5f86,#a8bfd6 55%,#294566)}
.cap-item{position:absolute;width:200px}
.cap-item .ic{width:56px;height:56px;border-radius:8px;background:#fde8d8;display:flex;align-items:center;justify-content:center;margin-bottom:14px}
.cap-item h4{font-size:19px;font-weight:700;margin-bottom:8px;white-space:nowrap}
.cap-item p{font-size:14px;line-height:1.55}
.capabilities .pill{position:absolute;left:960px;top:612px;width:150px;height:40px;font-size:15px}

/* partners */
.partners{position:absolute;left:0;top:3092px;width:1200px;height:232px;background:var(--light)}
.partner{position:absolute;top:70px;width:168px;height:92px;background:#fff;border-radius:14px;display:flex;align-items:center;justify-content:center}
.partner span{width:96px;height:24px;border-radius:12px;background:#d4d8de}

/* resources */
.resources{position:absolute;left:0;top:3324px;width:1200px;height:840px}
.resources h2{position:absolute;left:64px;top:128px;font-size:60px;font-weight:600;color:var(--navy)}
.card{position:absolute;top:256px;width:328px}
.card .img{height:204px;border-bottom:6px solid var(--orange)}
.card .date{margin-top:24px;font-size:14px;color:var(--muted);display:flex;align-items:center;gap:8px}
.card h4{margin-top:8px;font-size:20px;font-weight:600;line-height:1.35;color:var(--navy)}
.card p{margin-top:10px;font-size:13px;line-height:1.6}
.card .pill{margin-top:12px;width:92px;height:26px;font-size:11px}

/* cta */
.cta{position:absolute;left:0;top:4164px;width:1200px;height:404px;background:var(--light);text-align:center}
.cta h2{margin-top:110px;font-size:58px;font-weight:600;line-height:1.2;color:var(--navy)}
.cta .pill{margin-top:26px;width:220px;height:64px}

/* footer */
.site-footer{position:absolute;left:0;top:4568px;width:1200px;height:392px;background:var(--navy);color:#fff}
.site-footer .brand{position:absolute;left:64px;top:120px;font-size:50px;color:#fff}
.site-footer .brand .mark{width:48px;height:48px}
.fcol{position:absolute;top:60px}
.fcol h4{font-size:20px;font-weight:700;color:#fff;margin-bottom:18px;white-space:nowrap}
.fcol li{list-style:none;font-size:15px;line-height:2;display:flex;align-items:center;gap:12px}
.fcol li::before{content:"";width:8px;height:8px;border-radius:50%;background:var(--orange)}
.contact-row{display:flex;gap:14px;margin-bottom:16px;font-size:14px;line-height:1.4}
.contact-row .ci{width:30px;height:30px;border-radius:6px;background:var(--orange);flex:none;display:flex;align-items:center;justify-content:center}
.footer-bar{position:absolute;left:0;bottom:0;width:1200px;height:56px;border-top:1px solid rgba(255,255,255,.15);font-size:13px;padding:18px 64px}
.socials{position:absolute;right:64px;top:16px;display:flex;gap:10px}
.socials span{width:24px;height:24px;background:#fff;border-radius:4px}
</style>
</head>
<body>

<header class="site-header">
  <div class="brand"><span class="mark"></span>BrimCore</div>
  <div class="search">Search...</div>
  <div class="signin">Sign In</div>
  <nav class="nav">
    <span class="active">HOME</span><span>PLATFORM ▾</span><span>SOLUTIONS ▾</span><span>RESOURCES ▾</span><span>SUPPORT ▾</span><span>CONTACT US</span>
  </nav>
</header>

<section class="hero" role="img" aria-label="Person standing before a wall of monitoring screens in a control room">
  <div class="welcome">Welcome To</div>
  <h1>BRIMCORE</h1>
  <p>Lorem ipsum dolor sit amet, consectetur adipiscing elit, sed do eiusmod tempor inci didunt ut labore et dolore magna aliqua.</p>
  <a class="pill orange">Learn More</a>
</section>

<section class="features">
  <div class="feature">
    <div class="icon orange"><svg width="54" height="54" viewBox="0 0 24 24" fill="none" stroke="#fff" stroke-width="2"><path d="M12 2l8 3v6c0 5-3.5 9-8 11-4.5-2-8-6-8-11V5z"/><rect x="9" y="11" width="6" height="5"/><path d="M10 11V9a2 2 0 014 0v2"/></svg></div>
    <h3>Data Privacy</h3>
  </div>
  <div class="feature">
    <div class="icon navy"><svg width="54" height="54" viewBox="0 0 24 24" fill="none" stroke="#fff" stroke-width="2"><circle cx="12" cy="12" r="9"/><path d="M8 12l3 3 5-6"/></svg></div>
    <h3>Trustworthy Interactions</h3>
  </div>
  <div class="feature">
    <div class="icon orange"><svg width="54" height="54" viewBox="0 0 24 24" fill="none" stroke="#fff" stroke-width="2"><circle cx="12" cy="12" r="9"/><circle cx="12" cy="12" r="5"/><circle cx="12" cy="12" r="1.5" fill="#fff"/></svg></div>
    <h3>Precision &amp; Compliance</h3>
  </div>
  <div class="feature">
    <div class="icon navy"><svg width="54" height="54" viewBox="0 0 24 24" fill="none" stroke="#fff" stroke-width="2"><rect x="3" y="4" width="18" height="16" rx="2"/><path d="M9 10l-3 2 3 2M15 10l3 2-3 2"/></svg></div>
    <h3>Low-Code</h3>
  </div>
</section>

<section class="welcome-block">
  <div class="emblem" role="img" aria-label="BrimCore emblem area"></div>
  <h2>Welcome to<br><span class="orange-t">BrimCore</span></h2>
  <p class="lead">Lorem ipsum dolor sit amet, consectetur adipiscing elit. Etiam in vestibulum urna.</p>
  <p class="body">Lorem ipsum dolor sit amet, consectetur adipiscing elit, sed do eiusmod tempor incididunt ut labore et dolore magna aliqua. Ut enim ad minim veniam, quis nostrud exercitation ullamco laboris nisi ut aliquip ex ea commodo consequat. Duis aute irure dolor in reprehenderit in voluptate velit esse cillum dolore eu fugiat nulla pariatur. Excepteur sint occaecat cupidatat non proident, sunt in culpa qui officia deserunt mollit anim id est laborum.</p>
  <a class="pill navy">Read More</a>
</section>

<section class="platform">
  <h2>One Platform<br><span class="orange-t">for All Your<br>Needs</span></h2>
  <p>Lorem ipsum dolor sit amet, consectetur adipi scing elit, sed do eiusmod tempor incididunt ut labore et dolore magna.</p>
  <a class="pill navy">View All Platforms</a>
  <div class="slide" style="left:460px;background:linear-gradient(160deg,#8fb0cc,#3c5f80)" role="img" aria-label="Hand using a tablet with a digital interface"><div class="cap">Workforce Authorization</div></div>
  <div class="slide" style="left:772px;background:linear-gradient(160deg,#c5d3e0,#5d7a96)" role="img" aria-label="Desk with computer monitors in an office"><div class="cap">Customer Authorization</div></div>
  <div class="slide" style="left:1084px;width:140px;background:linear-gradient(160deg,#6f8eac,#24405f)" role="img" aria-label="Data center servers"><div class="cap">Data</div></div>
  <div class="arrow" style="left:448px;top:288px;background:var(--orange)"><svg width="22" height="22" viewBox="0 0 24 24" fill="none" stroke="#fff" stroke-width="3"><path d="M15 5l-7 7 7 7"/></svg></div>
  <div class="arrow" style="left:1132px;top:288px;background:var(--navy)"><svg width="22" height="22" viewBox="0 0 24 24" fill="none" stroke="#fff" stroke-width="3"><path d="M9 5l7 7-7 7"/></svg></div>
</section>

<section class="capabilities">
  <h2>BrimCore<br><span class="orange-t">Capabilities</span></h2>
  <p class="intro">Lorem ipsum dolor sit amet, consectetur adipi scing elit, sed do eiusmod tempor incididunt ut labore et dolore magna aliqua. Lorem ipsum dolor sit amet, consectetur adipiscing elit, sed do eiusmod tempor incididunt ut labore et dolore magna aliqua. Lorem ipsum dolor sit amet, consectetur adipi scing elit, sed do eiusmod tempor incididunt ut labore.</p>
  <div class="photo" role="img" aria-label="Operator with headset working at screens in a network operations center"></div>
  <div class="cap-item" style="left:490px;top:276px"><div class="ic"><svg width="28" height="28" viewBox="0 0 24 24" fill="none" stroke="#ee7d2b" stroke-width="2"><path d="M3 21h18M5 21V10M12 21V10M19 21V10M2 9l10-6 10 6z"/></svg></div><h4>Governance</h4><p>Lorem ipsum dolor sit amet, consectetur adipiscing elit ut elementum sagittis.</p></div>
  <div class="cap-item" style="left:712px;top:276px"><div class="ic"><svg width="28" height="28" viewBox="0 0 24 24" fill="none" stroke="#ee7d2b" stroke-width="2"><rect x="3" y="3" width="8" height="8"/><rect x="13" y="3" width="8" height="5"/><rect x="13" y="10" width="8" height="11"/><rect x="3" y="13" width="8" height="8"/></svg></div><h4>Dashboard</h4><p>Lorem ipsum dolor sit amet, consectetur adipiscing elit ut elementum sagittis.</p></div>
  <div class="cap-item" style="left:932px;top:276px"><div class="ic"><svg width="28" height="28" viewBox="0 0 24 24" fill="none" stroke="#ee7d2b" stroke-width="2"><circle cx="12" cy="8" r="4"/><path d="M4 21c0-4 4-6 8-6s8 2 8 6"/></svg></div><h4>Admin Assistant</h4><p>Lorem ipsum dolor sit amet, consectetur adipiscing elit ut elementum sagittis.</p></div>
  <div class="cap-item" style="left:490px;top:498px"><div class="ic"><svg width="28" height="28" viewBox="0 0 24 24" fill="none" stroke="#ee7d2b" stroke-width="2"><path d="M12 3l10 18H2z"/><path d="M12 10v5M12 17.5v.5"/></svg></div><h4>Threat Detection</h4><p>Lorem ipsum dolor sit amet, consectetur adipiscing elit ut elementum sagittis.</p></div>
  <div class="cap-item" style="left:712px;top:498px"><div class="ic"><svg width="28" height="28" viewBox="0 0 24 24" fill="none" stroke="#ee7d2b" stroke-width="2"><path d="M6 2h9l4 4v16H6z"/><path d="M9 11h7M9 15h7"/></svg></div><h4>Documentation</h4><p>Lorem ipsum dolor sit amet, consectetur adipiscing elit ut elementum sagittis.</p></div>
  <a class="pill orange">View More</a>
</section>

<section class="partners">
  <div class="arrow" style="left:48px;top:88px;width:52px;height:52px;border:2px solid var(--orange)"><svg width="20" height="20" viewBox="0 0 24 24" fill="none" stroke="#ee7d2b" stroke-width="3"><path d="M15 5l-7 7 7 7"/></svg></div>
  <div class="partner" style="left:140px"><span></span></div>
  <div class="partner" style="left:328px"><span></span></div>
  <div class="partner" style="left:516px"><span></span></div>
  <div class="partner" style="left:704px"><span></span></div>
  <div class="partner" style="left:892px"><span></span></div>
  <div class="arrow" style="left:1100px;top:88px;width:52px;height:52px;background:var(--orange)"><svg width="20" height="20" viewBox="0 0 24 24" fill="none" stroke="#fff" stroke-width="3"><path d="M9 5l7 7-7 7"/></svg></div>
</section>

<section class="resources">
  <h2>Featured <span class="orange-t">Resources</span></h2>
  <div class="arrow" style="left:1012px;top:140px;width:52px;height:52px;border:2px solid var(--orange)"><svg width="20" height="20" viewBox="0 0 24 24" fill="none" stroke="#ee7d2b" stroke-width="3"><path d="M15 5l-7 7 7 7"/></svg></div>
  <div class="arrow" style="left:1076px;top:140px;width:52px;height:52px;background:var(--navy)"><svg width="20" height="20" viewBox="0 0 24 24" fill="none" stroke="#fff" stroke-width="3"><path d="M9 5l7 7-7 7"/></svg></div>
  <article class="card" style="left:64px"><div class="img" style="background:linear-gradient(135deg,#2c5d8f,#7fb0da)" role="img" aria-label="Hands using a smartphone with glowing data icons"></div><div class="date"><svg width="14" height="14" viewBox="0 0 24 24" fill="none" stroke="#ee7d2b" stroke-width="2"><rect x="3" y="5" width="18" height="16"/><path d="M3 10h18M8 3v4M16 3v4"/></svg>February 27, 2022</div><h4>Lorem ipsum dolor sit amet, consectetur adipiscing</h4><p>Lorem ipsum dolor sit amet, consectetur adipiscing elit, sed do eiusmod tempor incididunt ut labore.</p><a class="pill orange">Read More</a></article>
  <article class="card" style="left:436px"><div class="img" style="background:linear-gradient(135deg,#3a3f48,#c98a4a)" role="img" aria-label="Automated warehouse with conveyor lines"></div><div class="date"><svg width="14" height="14" viewBox="0 0 24 24" fill="none" stroke="#ee7d2b" stroke-width="2"><rect x="3" y="5" width="18" height="16"/><path d="M3 10h18M8 3v4M16 3v4"/></svg>February 27, 2022</div><h4>Lorem ipsum dolor sit amet, consectetur adipiscing</h4><p>Lorem ipsum dolor sit amet, consectetur adipiscing elit, sed do eiusmod tempor incididunt ut labore.</p><a class="pill orange">Read More</a></article>
  <article class="card" style="left:808px"><div class="img" style="background:linear-gradient(135deg,#173049,#5c88b0)" role="img" aria-label="Person viewing large monitoring displays"></div><div class="date"><svg width="14" height="14" viewBox="0 0 24 24" fill="none" stroke="#ee7d2b" stroke-width="2"><rect x="3" y="5" width="18" height="16"/><path d="M3 10h18M8 3v4M16 3v4"/></svg>February 27, 2022</div><h4>Lorem ipsum dolor sit amet, consectetur adipiscing</h4><p>Lorem ipsum dolor sit amet, consectetur adipiscing elit, sed do eiusmod tempor incididunt ut labore.</p><a class="pill orange">Read More</a></article>
</section>

<section class="cta">
  <h2>Lorem Ipsum Dolor Sit Amet,<br><span class="orange-t">Consectetur Adipiscing Elit</span></h2>
  <a class="pill navy">Learn More</a>
</section>

<footer class="site-footer">
  <div class="brand"><span class="mark"></span>BrimCore</div>
  <div class="fcol" style="left:420px"><h4>WHY <span class="orange-t">BRIMCORE</span></h4><ul><li>Customer Stories</li><li>Solutions</li><li>Industries</li><li>Analyst Reports</li></ul></div>
  <div class="fcol" style="left:672px"><h4>QUICK <span class="orange-t">LINKS</span></h4><ul><li>Platforms</li><li>Solutions</li><li>Resources</li><li>Support</li><li>Contact Us</li></ul></div>
  <div class="fcol" style="left:872px"><h4>CONTACT <span class="orange-t">US</span></h4>
    <div class="contact-row"><span class="ci"><svg width="16" height="16" viewBox="0 0 24 24" fill="#fff"><path d="M6 2l4 4-2 3c1 3 4 6 7 7l3-2 4 4-3 4C10 22 2 14 2 5z"/></svg></span><span>CALL US<br>(555) 310-4826</span></div>
    <div class="contact-row"><span class="ci"><svg width="16" height="16" viewBox="0 0 24 24" fill="none" stroke="#fff" stroke-width="2"><rect x="2" y="5" width="20" height="14"/><path d="M2 6l10 7 10-7"/></svg></span><span>EMAIL US<br>hello@brimcore.example</span></div>
    <div class="contact-row"><span class="ci"><svg width="16" height="16" viewBox="0 0 24 24" fill="#fff"><path d="M12 2a7 7 0 017 7c0 5-7 13-7 13S5 14 5 9a7 7 0 017-7z"/></svg></span><span>Address line placeholder<br>address line two here</span></div>
  </div>
  <div class="footer-bar">Copyright © 2025 All Rights Reserved By BrimCore
    <div class="socials"><span></span><span></span><span></span><span></span><span></span></div>
  </div>
</footer>

</body>
</html>
```